Kettle Ledger Business Card design

We need a stand out business card design for Accounting practice based in Australia specialising in pubs, clubs and hotels. We help venues maximise margins, create time and manage cashflow. One club we have been working with for the last 6 months has increased revenue by 3% and margin by 5% in this time frame. We have a back office outsourced system that costs less than having a full time employee and also allows the venues the added benefit of:<br/>-using the office space to become a revenue generating opportunity. <br/>-a complete system to enhance governance, accountability and efficiency within their operation<br/>-52 weeks cover so no hassle to cover annual/sick .. leave<br/><br/>We would like to see designs that use the colours of our logo (green & blue).
Target Market(s)
Australian Pubs, Clubs & Hotels abookkeeping, accounting and tax services
Industry/Entity Type
Accountant
Contact Information for Business Card
Miriam Oakley CPA
Principal
Accountant Tax Agent
Miriam@KettleLedger-example.com.au
0418693142
www.kettleledger-example.com.au
Accounting / Payroll / Tax / SMSF / Technology
Colors
Designer to choose colors to be used in the design.
Look and feel
Each slider illustrates characteristics of the customer's brand and the style your logo design should communicate.

```html
<!DOCTYPE html>
<html lang="en">
<head>
<meta charset="utf-8">
<title>Kettle Ledger – Business Card</title>
<link href="https://fonts.googleapis.com/css2?family=Arimo:ital,wght@0,400;0,700;1,700&family=Montserrat:ital,wght@0,800;1,700&display=swap" rel="stylesheet">
<style>
  :root {
    --brand-blue: #23428e;
    --brand-green: #12803f;
    --panel-grey: #e5e5e7;
    --paper: #ffffff;
    --page: #ffffff;
  }
  * { margin: 0; padding: 0; box-sizing: border-box; }
  html, body { width: 1068px; height: 1200px; overflow: hidden; background: var(--page); }
  .canvas { position: relative; width: 1068px; height: 1200px; }

  .card { position: absolute; left: 150px; width: 769px; height: 433px; box-shadow: 0 1px 4px rgba(0,0,0,.2); }
  .card--front { top: 95px; background: var(--paper); }
  .card--back { top: 600px; height: 440px; background: var(--brand-blue); }

  /* front */
  .front-panel { position: absolute; left: 0; top: 0; width: 323px; height: 433px; background: var(--brand-blue); border-top-right-radius: 64px; }
  .front-grey { position: absolute; left: 323px; top: 14px; width: 428px; height: 403px; background: var(--panel-grey); }

  .wordmark { position: absolute; display: flex; align-items: center; gap: 12px; }
  .wordmark__dot { width: 52px; height: 52px; border-radius: 50%; background: var(--brand-green); flex: none; }
  .wordmark__name { font-family: "Montserrat", sans-serif; font-weight: 800; color: var(--brand-blue); font-size: 38px; line-height: 0.98; letter-spacing: -0.5px; }
  .card--front .wordmark { left: 450px; top: 158px; }

  .front-url { position: absolute; left: 426px; top: 266px; font-family: "Arimo", sans-serif; font-size: 19px; color: var(--brand-blue); }

  /* back */
  .back-contact { position: absolute; left: 12px; top: 11px; width: 341px; height: 417px; background: var(--panel-grey); }
  .back-contact__inner { position: absolute; left: 7px; top: 7px; width: 332px; height: 403px; background: var(--paper); }
  .back-services { position: absolute; left: 351px; top: 80px; width: 409px; height: 347px; background: var(--panel-grey); }
  .title-tab { position: absolute; left: 294px; top: 0; width: 466px; height: 80px; background: var(--brand-blue); border-bottom-left-radius: 70px; }
  .title-tab__text { position: absolute; right: 24px; top: 22px; font-family: "Arimo", sans-serif; font-style: italic; font-weight: 700; font-size: 34px; color: var(--paper); white-space: nowrap; }

  .card--back .wordmark { left: 36px; top: 40px; }
  .person { position: absolute; left: 7px; width: 332px; text-align: center; font-family: "Arimo", sans-serif; color: var(--brand-blue); }
  .person__name { top: 170px; font-size: 37px; }
  .person__role { top: 218px; font-size: 26px; }
  .person__phone { top: 268px; font-size: 34px; font-weight: 700; color: var(--brand-green); }
  .person__links { top: 361px; font-size: 17px; line-height: 1.1; }

  .services { position: absolute; left: 416px; top: 146px; list-style: none; }
  .services__item { display: flex; align-items: center; gap: 16px; height: 43.3px; font-family: "Montserrat", sans-serif; font-style: italic; font-weight: 700; font-size: 33px; color: var(--brand-blue); }
  .services__bullet { width: 20px; height: 20px; border: 2px solid var(--brand-green); border-radius: 50%; flex: none; }
</style>
</head>
<body>
<div class="canvas">

  <section class="card card--front">
    <div class="front-panel" role="img" aria-label="Large white outline decoration of the brand symbol on blue"></div>
    <div class="front-grey"></div>
    <div class="wordmark">
      <span class="wordmark__dot"></span>
      <span class="wordmark__name">Kettle<br>Ledger</span>
    </div>
    <p class="front-url">www.kettleledger-example.com.au</p>
  </section>

  <section class="card card--back">
    <div class="back-contact">
      <div class="back-contact__inner"></div>
    </div>
    <div class="back-services"></div>
    <div class="title-tab"><span class="title-tab__text">Accountant Tax Agent</span></div>

    <div class="wordmark">
      <span class="wordmark__dot"></span>
      <span class="wordmark__name">Kettle<br>Ledger</span>
    </div>

    <p class="person person__name">Miriam Oakley</p>
    <p class="person person__role">CPA Principal</p>
    <p class="person person__phone">041 869 3142</p>
    <p class="person person__links">Miriam@KettleLedger-example.com.au<br>www.kettleledger-example.com.au</p>

    <ul class="services">
      <li class="services__item"><span class="services__bullet"></span>Accounting</li>
      <li class="services__item"><span class="services__bullet"></span>Payroll</li>
      <li class="services__item"><span class="services__bullet"></span>Tax</li>
      <li class="services__item"><span class="services__bullet"></span>SMSF</li>
      <li class="services__item"><span class="services__bullet"></span>Technology</li>
    </ul>
  </section>

</div>
</body>
</html>
```